Brilliant Design Needed For Stand Up Pouch - Drink Mix

We need a layout for our resealable stand-up pouch that holds our powered sports drink mix. Target audience is endurance athletes that enjoy marathon running, cycling, mountain biking, hiking and triathlon. Secondary audience are participants in team sports such soccer, lacrosse, football and basketball. Please review the attached project brief for full details. Thanks!

Target Market(s)

50/50 male/female, ages 20-50, USA, succesful, driven, educated. Active, healthy, athletic, outdoor lifestyle.

Industry/Entity Type

Fitness

Font styles to use
Sans Serif

Colors
33a6d7
3277b5
abd037

Requirements
Must have
• Please review the attached project brief for full details.
Nice to have
Should not have

```html
<!DOCTYPE html>
<html lang="en">
<head>
<meta charset="utf-8">
<title>Korvana Endurance Formula Pouch</title>
<link rel="stylesheet" href="https://fonts.googleapis.com/css2?family=Exo+2:ital,wght@0,700;0,800;1,800;1,900&family=Roboto:wght@400;700&display=swap">
<style>
  :root {
    --navy: #1d3f5c;
    --cyan: #33a6d7;
    --blue: #3277b5;
    --lime: #abd037;
    --magenta: #e0208f;
    --ink: #111111;
    --white: #ffffff;
    --silver-light: #f4f4f4;
    --silver-dark: #9a9a9a;
    --gold: #f3d21a;
  }
  * { margin: 0; padding: 0; box-sizing: border-box; }
  html, body { width: 888px; height: 1200px; overflow: hidden; background: var(--white); }
  .pouch { position: relative; width: 888px; height: 1200px; background: var(--white); font-family: "Roboto", Arial, sans-serif; }

  .brand-name {
    position: absolute; top: 190px; left: 0; width: 888px; text-align: center;
    font-family: "Exo 2", Arial, sans-serif; font-weight: 800; font-size: 80px;
    letter-spacing: 4px; color: var(--navy);
  }

  .formula-banner {
    position: absolute; top: 298px; left: 68px; width: 764px; height: 110px;
    border-radius: 10px;
    background: linear-gradient(180deg, var(--silver-light) 0%, #d6d6d6 45%, var(--silver-dark) 100%);
    box-shadow: inset 0 0 0 2px #bdbdbd;
  }
  .formula-tagline {
    position: absolute; top: 18px; left: 42px;
    font-family: "Exo 2", Arial, sans-serif; font-style: italic; font-weight: 800;
    font-size: 19px; letter-spacing: 1px; color: var(--ink);
  }
  .formula-title {
    position: absolute; top: 40px; left: 40px;
    font-family: "Exo 2", Arial, sans-serif; font-style: italic; font-weight: 900;
    font-size: 58px; letter-spacing: 2px; color: var(--magenta);
  }

  .hero-panel { position: absolute; top: 418px; left: 52px; width: 770px; height: 682px; }

  .rider-art {
    position: absolute; top: 515px; left: 258px; width: 320px; height: 490px;
    border-radius: 140px 140px 40px 40px;
    background: radial-gradient(ellipse at 50% 45%, #0a0f2a 0%, #141a3a 55%, rgba(20,26,58,0.35) 100%);
  }

  .quality-badge { position: absolute; top: 535px; left: 90px; width: 130px; height: 160px; }

  .feature-list { position: absolute; top: 510px; left: 555px; list-style: none; }
  .feature {
    display: flex; align-items: center; height: 76px; margin-bottom: 8px;
  }
  .feature-icon {
    width: 52px; height: 52px; border-radius: 50%; flex: none;
    background: radial-gradient(circle at 35% 30%, #ffffff, #a9a9a9 75%);
    box-shadow: 0 0 0 2px #6d6d6d;
    display: flex; align-items: center; justify-content: center;
  }
  .feature-text { margin-left: 18px; font-size: 16px; line-height: 21px; color: var(--white); }

  .info-bar {
    position: absolute; top: 1028px; left: 120px; width: 690px; height: 66px;
    background: linear-gradient(90deg, #fff200 0%, #e6ea20 30%, var(--lime) 55%, var(--cyan) 100%);
    display: flex; align-items: center;
  }
  .net-label {
    padding-left: 14px; width: 74px; font-weight: 700; font-size: 18px; line-height: 24px; color: var(--ink);
    border-right: 2px solid var(--ink);
  }
  .net-value { padding-left: 12px; width: 190px; font-weight: 700; font-size: 18px; line-height: 24px; color: var(--ink); }
  .flavor {
    font-family: "Exo 2", Arial, sans-serif; font-style: italic; font-weight: 800;
    font-size: 24px; line-height: 26px; color: #2f8a2a;
  }
</style>
</head>
<body>
<main class="pouch">
  <div class="brand-name">KORVANA</div>

  <section class="formula-banner">
    <p class="formula-tagline">HYDRATION BY DURATION</p>
    <h1 class="formula-title">ENDURANCE FORMULA</h1>
  </section>

  <svg class="hero-panel" viewBox="0 0 770 682" aria-hidden="true">
    <defs>
      <linearGradient id="panelFill" x1="0" y1="0" x2="1" y2="0">
        <stop offset="0" stop-color="#000000"/>
        <stop offset="0.3" stop-color="#1e2a7a"/>
        <stop offset="0.6" stop-color="#3277b5"/>
        <stop offset="1" stop-color="#19aee6"/>
      </linearGradient>
      <linearGradient id="swooshFill" x1="0" y1="0" x2="1" y2="1">
        <stop offset="0" stop-color="#ffffff"/>
        <stop offset="1" stop-color="#bfbfbf"/>
      </linearGradient>
    </defs>
    <rect width="770" height="682" fill="url(#panelFill)"/>
    <path d="M0 0 H360 C220 40 120 140 60 300 C30 380 10 480 0 600 Z" fill="#000000"/>
    <path d="M0 610 C20 330 170 90 430 0 L470 0 C230 90 70 320 30 682 H0 Z" fill="url(#swooshFill)"/>
  </svg>

  <div class="rider-art" role="img" aria-label="Silhouette of a cyclist riding a road bike"></div>

  <svg class="quality-badge" viewBox="0 0 130 160" aria-hidden="true">
    <circle cx="65" cy="60" r="52" fill="var(--gold)"/>
    <path d="M20 95 H110 L100 135 H30 Z" fill="#e2b90f"/>
  </svg>

  <ul class="feature-list">
    <li class="feature">
      <span class="feature-icon">
        <svg width="30" height="20" viewBox="0 0 30 20"><rect x="1" y="2" width="25" height="16" rx="2" fill="none" stroke="#111" stroke-width="2"/><rect x="26" y="7" width="3" height="6" fill="#111"/><path d="M8 10 l4 4 l8 -8" fill="none" stroke="#111" stroke-width="2"/></svg>
      </span>
      <span class="feature-text">Advanced<br>Hydration System</span>
    </li>
    <li class="feature">
      <span class="feature-icon">
        <svg width="24" height="30" viewBox="0 0 24 30"><path d="M2 2 H22 L19 28 H5 Z" fill="none" stroke="#111" stroke-width="2"/><path d="M4 12 H20 L18 27 H6 Z" fill="#111"/></svg>
      </span>
      <span class="feature-text">Makes 27, 12 fl oz<br>Servings</span>
    </li>
    <li class="feature">
      <span class="feature-icon">
        <svg width="36" height="22" viewBox="0 0 36 22"><rect x="3" y="3" width="6" height="16" fill="#111"/><rect x="27" y="3" width="6" height="16" fill="#111"/><rect x="9" y="9" width="18" height="4" fill="#111"/><rect x="0" y="7" width="3" height="8" fill="#111"/><rect x="33" y="7" width="3" height="8" fill="#111"/></svg>
      </span>
      <span class="feature-text">Recommended For<br>Workouts<br>Lasting 1 Hour</span>
    </li>
  </ul>

  <section class="info-bar">
    <p class="net-label">NET<br>WT.</p>
    <p class="net-value">15.5 OZ<br>(440G)</p>
    <p class="flavor">Lemon-Lime with<br>other natural flavors</p>
  </section>
</main>
</body>
</html>
```